'Wedding Business" Business Card Design

dj services for weddings and parties, uplighting, event planning, day of coordination for weddings, photography for weddings and other events.

Would like raised print and metallic also if possible. Elegant design, yet modern. This is a wedding business and should describe our goals and main services - DJ/lighting, wedding and event planning, photography. slogan "Simply Incredible, Incredibly simple" or "Your Dreams. Our Experience. The Perfect Match" Our goal is to provide multiple services to make it easier for the bride and groom almost like a one stop shop. Feel free to use the slogan or leave it out , we just want to really stand out against the competition. You can also get more info on our website www.bluelarkproductions.com - we are working to get the bluelarkct.com site pointed to our current site!

there should be 2 files attached, if they did not go through please email events@bluelarkct.com or bluelarkproductions@mailbox.test
Updates

Thank you all for your help, we have decided what we like but would like to make some changes, we need to order these asap so please let us know if you can help.

Reason: Wasn't able to pick it out in time! So Sorry but we know what we want!!

Industry/Entity Type

Business

Contact Information for Business Card

Trevor and Mallory Quenby
555-318-2746
555-207-4831
Blue Lark Productions, Events, & Photography
EMAIL:Events@BlueLarkCT.com
www.bluelarkct.com

```html
<!DOCTYPE html>
<html lang="en">
<head>
<meta charset="utf-8">
<title>Blue Lark Productions – Business Card</title>
<link rel="stylesheet" href="https://fonts.googleapis.com/css2?family=Raleway:wght@300;400&display=swap">
<style>
  :root {
    --stage: #e9e6e1;
    --card-black: #050507;
    --card-sheen: #1f2029;
    --violet-glow: #2a2b58;
    --silver: #e4e6ee;
    --silver-soft: #b9bcc8;
    --ornament: #8f93a6;
    --rule: #9a9cab;
  }
  * { box-sizing: border-box; margin: 0; padding: 0; }
  html, body { width: 1200px; height: 900px; overflow: hidden; }
  body {
    background: var(--stage);
    font-family: "Raleway", sans-serif;
    display: flex;
    flex-direction: column;
    align-items: center;
    justify-content: center;
    gap: 46px;
  }
  .card {
    position: relative;
    width: 660px;
    height: 377px;
    border-radius: 6px;
    overflow: hidden;
    color: var(--silver);
    box-shadow: 0 10px 24px rgba(0,0,0,.25);
  }

  /* Front */
  .card-front {
    background:
      radial-gradient(ellipse 55% 70% at 62% 45%, var(--violet-glow) 0%, transparent 70%),
      linear-gradient(135deg, var(--card-sheen) 0%, var(--card-black) 55%, var(--card-black) 100%);
  }
  .card-front .brand-mark {
    position: absolute;
    left: 44px;
    top: 50%;
    transform: translateY(-50%);
    display: flex;
    align-items: center;
    gap: 12px;
  }
  .brand-dot {
    width: 14px; height: 14px;
    border-radius: 50%;
    background: #5a5fb0;
  }
  .brand-name {
    font-weight: 300;
    font-size: 40px;
    letter-spacing: 2px;
    color: var(--silver);
  }
  .contact-block {
    position: absolute;
    right: 34px;
    top: 0; bottom: 0;
    width: 330px;
    display: flex;
    flex-direction: column;
    align-items: center;
    justify-content: center;
    text-align: center;
  }
  .ornament {
    width: 150px;
    height: 40px;
    border-radius: 20px;
    background: radial-gradient(ellipse at center, var(--ornament) 0%, rgba(143,147,166,.25) 55%, transparent 75%);
  }
  .ornament.top { margin-bottom: 12px; }
  .ornament.bottom { margin-top: 12px; }
  .company-name {
    font-weight: 400;
    font-size: 22px;
    letter-spacing: 1px;
    text-transform: uppercase;
  }
  .company-tagline {
    font-weight: 300;
    font-size: 15px;
    letter-spacing: 1.5px;
    text-transform: uppercase;
    margin-bottom: 8px;
  }
  .contact-line {
    font-weight: 300;
    font-size: 15px;
    line-height: 1.45;
    color: var(--silver);
  }
  .contact-line.people { color: var(--silver-soft); }

  /* Back */
  .card-back {
    background: linear-gradient(160deg, #0d0d11 0%, var(--card-black) 60%);
  }
  .card-back .brand-mark {
    position: absolute;
    left: 0; right: 0;
    top: 92px;
    display: flex;
    justify-content: center;
    align-items: center;
    gap: 12px;
  }
  .slogan-block {
    position: absolute;
    left: 40px; right: 40px;
    bottom: 64px;
    text-align: center;
  }
  .slogan {
    font-weight: 400;
    font-size: 21px;
    letter-spacing: .5px;
    color: var(--silver);
    padding-bottom: 8px;
    border-bottom: 1px solid var(--rule);
  }
  .slogan .sep { font-size: 13px; vertical-align: middle; margin: 0 6px; }
  .services {
    margin-top: 10px;
    font-weight: 300;
    font-size: 13px;
    line-height: 1.5;
    color: var(--silver-soft);
  }
</style>
</head>
<body>

  <section class="card card-front" aria-label="Business card front">
    <div class="brand-mark">
      <span class="brand-dot"></span>
      <span class="brand-name">Blue Lark</span>
    </div>
    <div class="contact-block">
      <div class="ornament top" role="img" aria-label="Silver filigree scroll ornament"></div>
      <p class="company-name">Blue Lark Productions</p>
      <p class="company-tagline">Events, &amp; Photography</p>
      <p class="contact-line people">Trevor and Mallory Quenby</p>
      <p class="contact-line">555-318-2746</p>
      <p class="contact-line">555-207-4831</p>
      <p class="contact-line">Email:Events@BlueLarkCT.com</p>
      <p class="contact-line">www.bluelarkct.com</p>
      <div class="ornament bottom" role="img" aria-label="Silver filigree scroll ornament"></div>
    </div>
  </section>

  <section class="card card-back" aria-label="Business card back">
    <div class="brand-mark">
      <span class="brand-dot"></span>
      <span class="brand-name">Blue Lark</span>
    </div>
    <div class="slogan-block">
      <p class="slogan">Your Dreams <span class="sep">●</span> Our Experience <span class="sep">●</span> The Perfect Match</p>
      <p class="services">DJ services for weddings and parties, uplighting, event planning<br>day of coordination for weddings, photography for weddings and other events</p>
    </div>
  </section>

</body>
</html>
```